Business Card Design and stationary (thank you cards)

I am basically starting a "handyman" business but have a little ego issue with that term. I have been a professional in the design and construction business for 30 years. I want simple…I will define the scope of work I do as i move forward, and it can vary and i want it to vary.

Target Market(s)

Homeowners mostly

Industry/Entity Type

Business

Contact Information for Business Card

Company Name is "Ridgewell Works" Dale R. Hobbins, 42 Bellamy Orchard Lane, Millbrook, Vt, 05731 (but I may want to use a PO Box), Phone is 802-555-0172, email is dhobbins418@quillpost.example,

Font styles to use
Sans Serif

Requirements
Should not have
• anything pre designed….hammers or whatever…custom lines to make home features as shone but simple and elegant

```html
<!DOCTYPE html>
<html lang="en">
<head>
<meta charset="utf-8">
<title>Ridgewell Works – Business Card</title>
<link rel="stylesheet" href="https://fonts.googleapis.com/css2?family=Exo+2:wght@500;600&family=Open+Sans:wght@400&display=swap">
<style>
  :root {
    --teal: #1d8190;
    --gold: #d29a25;
    --gold-deep: #b98318;
    --paper: #f7f7f5;
    --ink: #4a5558;
    --backdrop: #e9e6e1;
  }
  * { margin: 0; padding: 0; box-sizing: border-box; }
  html, body { width: 1200px; height: 566px; overflow: hidden; }
  body {
    background: var(--backdrop);
    display: flex;
    align-items: center;
    justify-content: center;
    gap: 60px;
    font-family: "Open Sans", sans-serif;
  }
  .card {
    position: relative;
    width: 500px;
    height: 286px;
    overflow: hidden;
    border-radius: 3px;
    box-shadow: 0 6px 18px rgba(0,0,0,.18);
  }
  .card-art { position: absolute; inset: 0; }
  .front-brand {
    position: absolute;
    left: 34px;
    bottom: 30px;
    display: flex;
    align-items: center;
    gap: 10px;
    color: #fff;
    font-family: "Exo 2", sans-serif;
    font-weight: 600;
    font-size: 26px;
    letter-spacing: .3px;
    white-space: nowrap;
  }
  .brand-mark {
    width: 12px; height: 12px;
    background: #fff;
  }
  .back { background: var(--paper); }
  .back-brand {
    position: absolute;
    right: 26px;
    top: 50%;
    transform: translate(50%, -50%) rotate(90deg);
    color: #fff;
    font-family: "Exo 2", sans-serif;
    font-weight: 600;
    font-size: 17px;
    white-space: nowrap;
  }
  .contact {
    position: absolute;
    left: 44px;
    top: 64px;
  }
  .contact-name {
    font-family: "Exo 2", sans-serif;
    font-weight: 600;
    font-size: 25px;
    color: var(--teal);
    letter-spacing: 1px;
    text-transform: uppercase;
    margin-bottom: 20px;
  }
  .contact-list { list-style: none; }
  .contact-item {
    display: flex;
    align-items: flex-start;
    gap: 12px;
    font-size: 11.5px;
    line-height: 1.5;
    color: var(--ink);
    margin-bottom: 9px;
  }
  .contact-icon {
    flex: none;
    width: 16px; height: 16px;
    margin-top: 1px;
  }
</style>
</head>
<body>

  <section class="card front" aria-label="Card front">
    <svg class="card-art" viewBox="0 0 500 286" aria-hidden="true">
      <rect width="500" height="286" fill="var(--teal)"/>
      <polygon points="318,0 500,0 500,286 318,286 244,143" fill="var(--gold)"/>
      <polygon points="318,0 330,0 256,143 330,286 318,286 244,143" fill="var(--gold-deep)"/>
    </svg>
    <div class="front-brand"><span class="brand-mark"></span>Ridgewell Works</div>
  </section>

  <section class="card back" aria-label="Card back">
    <svg class="card-art" viewBox="0 0 500 286" aria-hidden="true">
      <polygon points="425,0 500,0 500,286 425,286 395,143" fill="var(--gold)"/>
      <polygon points="398,0 425,0 395,143 425,286 398,286 368,143" fill="var(--teal)"/>
    </svg>
    <div class="back-brand">Ridgewell Works</div>

    <div class="contact">
      <h1 class="contact-name">Dale R. Hobbins</h1>
      <ul class="contact-list">
        <li class="contact-item">
          <svg class="contact-icon" viewBox="0 0 16 16" aria-hidden="true">
            <rect x=".5" y=".5" width="15" height="15" fill="none" stroke="var(--teal)"/>
            <path d="M5 4h2l1 2.5-1.2.8a6 6 0 0 0 2 2l.8-1.2L12 9v2c0 .6-.5 1-1 1A7 7 0 0 1 4 5c0-.5.4-1 1-1z" fill="var(--teal)"/>
          </svg>
          <span>802-555-0172</span>
        </li>
        <li class="contact-item">
          <svg class="contact-icon" viewBox="0 0 16 16" aria-hidden="true">
            <rect x=".5" y=".5" width="15" height="15" fill="none" stroke="var(--teal)"/>
            <rect x="3.5" y="5" width="9" height="6.5" fill="none" stroke="var(--teal)"/>
            <path d="M3.5 5 8 8.6 12.5 5" fill="none" stroke="var(--teal)"/>
          </svg>
          <span>dhobbins418@quillpost.example</span>
        </li>
        <li class="contact-item">
          <svg class="contact-icon" viewBox="0 0 16 16" aria-hidden="true">
            <rect x=".5" y=".5" width="15" height="15" fill="none" stroke="var(--teal)"/>
            <path d="M8 3a3.2 3.2 0 0 0-3.2 3.2C4.8 8.8 8 13 8 13s3.2-4.2 3.2-6.8A3.2 3.2 0 0 0 8 3zm0 4.4a1.2 1.2 0 1 1 0-2.4 1.2 1.2 0 0 1 0 2.4z" fill="var(--teal)"/>
          </svg>
          <span>42 Bellamy Orchard Lane, Millbrook,<br>Vt, 05731</span>
        </li>
      </ul>
    </div>
  </section>

</body>
</html>
```